A property investment company, looking to provide lovely sustainable homes for familys and individua

For a small investment business i am starting which will buy and refurbish unloved houses and apartments to rent out or resell. the company name is my family surname (HARGREAVE). <br/>i would like the design to be simple with maybe some emphasis on an ethical and sustainable/environmentally friendly approach with a branding of maybe trees blended with some houses and or apartments.<br/>The colours i like for this design would be mainly green on either a white or black background.
Target Market(s)
This business card is to be used for professional people such as estate agents
mortgage brokers, solicitors and trades people.
Industry/Entity Type
Real Estate
Contact Information for Business Card
owner/director-Martin hargreave
e-mail-martin@hvholdings.co.uk
website-hargreavehomeholdings.co.uk
mobile-07700945318
landline-02079460581
Look and feel

```html
<!DOCTYPE html>
<html lang="en">
<head>
<meta charset="utf-8">
<title>Hargreave – Business Card</title>
<link rel="stylesheet" href="https://fonts.googleapis.com/css2?family=Della+Respira&display=swap">
<style>
  :root {
    --card-white: #ffffff;
    --band-black: #000000;
    --card-border: #8a8a8a;
    --name-green: #3db54a;
    --text-teal: #23a08c;
    --accent-green: #4cc04a;
    --brand-teal: #21a38d;
  }
  html, body {
    margin: 0;
    padding: 0;
    overflow: hidden;
    background: var(--card-white);
  }
  .card {
    position: relative;
    width: 1200px;
    height: 687px;
    box-sizing: border-box;
    border: 1px solid var(--card-border);
    background: var(--card-white);
    overflow: hidden;
    font-family: "Della Respira", Georgia, serif;
  }
  .brand {
    position: absolute;
    left: 38px;
    top: 78px;
    display: flex;
    align-items: center;
    gap: 12px;
  }
  .brand-name {
    font-size: 27px;
    letter-spacing: 5px;
    color: var(--brand-teal);
    line-height: 1;
  }
  .brand-square {
    width: 14px;
    height: 14px;
    background: var(--accent-green);
  }
  .holder {
    position: absolute;
    left: 0;
    right: 0;
    top: 238px;
  }
  .holder-name {
    position: absolute;
    left: 385px;
    top: 0;
    margin: 0;
    font-weight: normal;
    font-size: 57px;
    line-height: 1;
    color: var(--name-green);
    white-space: nowrap;
  }
  .holder-role {
    position: absolute;
    left: 474px;
    top: 80px;
    margin: 0;
    font-size: 30px;
    line-height: 1;
    color: var(--text-teal);
  }
  .contact-band {
    position: absolute;
    left: 0;
    right: 0;
    top: 560px;
    bottom: 0;
    background: var(--band-black);
    color: var(--text-teal);
  }
  .online {
    position: absolute;
    left: 35px;
    top: 24px;
    font-size: 29px;
    line-height: 46px;
  }
  .phones {
    position: absolute;
    right: 45px;
    top: 12px;
    display: grid;
    grid-template-columns: auto 8px auto;
    column-gap: 14px;
    row-gap: 8px;
    align-items: center;
    font-size: 30px;
  }
  .phone-label { text-align: right; }
  .phone-bar {
    width: 8px;
    height: 38px;
    background: var(--accent-green);
  }
  .phone-number { letter-spacing: 1px; }
</style>
</head>
<body>
  <div class="card">
    <div class="brand">
      <span class="brand-name">HARGREAVE</span>
      <span class="brand-square"></span>
    </div>

    <div class="holder">
      <h1 class="holder-name">Martin hargreave</h1>
      <p class="holder-role">Owner/director</p>
    </div>

    <div class="contact-band">
      <div class="online">
        <div class="email">martin@hvholdings.co.uk</div>
        <div class="website">www.hargreavehomeholdings.co.uk</div>
      </div>
      <div class="phones">
        <span class="phone-label">Mobile</span>
        <span class="phone-bar"></span>
        <span class="phone-number">07700945318</span>
        <span class="phone-label">Landline</span>
        <span class="phone-bar"></span>
        <span class="phone-number">02079460581</span>
      </div>
    </div>
  </div>
</body>
</html>
```